Management consultant needs to update look of website

Currently I have a great word press website but it needs an updated look. I have new text for the site in the attached word document. I also have a list of websites whose design, look, and organization i like as a guide for the designer. The final design should be simple, strong, clear, and project the idea that my brand is a powerful authority in this space. Current site = www.corvelstrategy.example

Target Market(s)

company owners / executives

Industry/Entity Type

Management Consulting

Number of Pages Required

3 page

Font styles to use
Serif

Colors

Designer to choose colors to be used in the design.

Requirements
Must have
• a simple and clear design and message. professional look. easy navigation. responsive to mobile devices. an easily implemented wordpress theme OR squarespace. use of my logo colors. though I am open to changing to a deep navy or charcoal logo image. source file uploaded.
Nice to have
• i like the cover photo and logo watermark on my current homepage. i like the google map with my logo on the current contact page. i like the animation as well. a great blend of the current site and something that is more seamless.

```html
<!DOCTYPE html>
<html lang="en">
<head>
<meta charset="utf-8">
<title>Quenmoor Leadership — Management Consulting</title>
<link href="https://fonts.googleapis.com/css2?family=Libre+Baskerville:wght@400;700&family=Open+Sans:wght@400;600&display=swap" rel="stylesheet">
<style>
:root{
  --gold:#b38f34;
  --gold-dark:#9a7a2a;
  --ink:#2a2a2a;
  --body:#6b6b6b;
  --light:#f1f1f1;
  --line:#dcdcdc;
  --footer:#2d2d2d;
  --footer-deep:#222222;
  --white:#ffffff;
}
*{box-sizing:border-box;margin:0;padding:0}
html,body{width:1200px;height:3820px;overflow:hidden}
body{background:var(--white);font-family:"Open Sans",Arial,sans-serif;color:var(--body);font-size:13px;line-height:1.6;position:relative}
.serif{font-family:"Libre Baskerville",Georgia,serif}
.abs{position:absolute}
.photo{position:absolute;border-radius:2px}
.btn{display:inline-block;background:var(--gold);color:var(--white);font-size:10px;font-weight:600;letter-spacing:1px;padding:7px 22px;border-radius:14px;text-transform:uppercase}

.site-header{position:absolute;top:0;left:0;width:1200px;height:64px;background:var(--white);display:flex;align-items:center;justify-content:space-between;padding:0 110px;z-index:3}
.brand{display:flex;align-items:center;gap:10px;font-family:"Libre Baskerville",Georgia,serif;color:var(--gold);font-size:15px}
.brand-dot{width:30px;height:30px;border-radius:50%;background:var(--gold)}
.main-nav{display:flex;gap:42px;font-size:10px;letter-spacing:1.5px;color:var(--ink)}
.main-nav .active{color:var(--gold)}

.hero{position:absolute;top:64px;left:0;width:1200px;height:576px;background:linear-gradient(160deg,#8c7f6f 0%,#6f6456 35%,#4f4a44 65%,#746b5f 100%)}
.hero-shade{position:absolute;inset:0;background:rgba(20,18,15,.35)}
.hero-intro{position:absolute;top:110px;left:280px;width:640px;text-align:center;color:#eee;font-size:12px}
.hero-quote{position:absolute;top:190px;left:0;width:1200px;text-align:center;color:var(--white);font-size:30px;line-height:1.25;text-transform:uppercase;font-weight:400}
.hero-cta{position:absolute;top:282px;left:0;width:1200px;text-align:center}

.mission{position:absolute;top:640px;left:0;width:1200px;height:320px;background:var(--gold);color:var(--white);text-align:center}
.mission h2{font-weight:400;margin-top:58px;font-size:17px;letter-spacing:1px}
.mission h2 span{display:block;font-size:27px;margin-top:4px}
.mission p{width:760px;margin:22px auto 0;font-size:12px;line-height:1.7}
.mission p + p{margin-top:10px}

.service h3{font-family:"Libre Baskerville",Georgia,serif;color:var(--gold);font-size:20px;font-weight:400;padding-bottom:10px;border-bottom:1px solid var(--line);margin-bottom:14px}
.service p{font-size:12px;margin-bottom:16px}
.service.right-align{text-align:right}

.section-title{position:absolute;left:0;width:1200px;text-align:center;color:var(--gold);font-family:"Libre Baskerville",Georgia,serif;font-size:22px;font-weight:400;letter-spacing:1px;text-transform:uppercase}
.section-title::after{content:"";display:block;width:60px;height:2px;background:var(--gold);margin:10px auto 0}

.blog-card{position:absolute;top:2180px;width:260px}
.blog-card .thumb{position:relative;height:160px;border-radius:2px}
.blog-card h4{font-family:"Libre Baskerville",Georgia,serif;color:var(--ink);font-size:13px;font-weight:400;margin-top:12px}
.blog-card .meta{font-size:10px;color:#9a9a9a;margin:2px 0 6px}
.blog-card p{font-size:11px;line-height:1.55}
.blog-card .more{color:var(--gold);font-size:11px;margin-top:6px;display:block}

.testimonials{position:absolute;top:2620px;left:0;width:1200px;height:420px;background:var(--light)}
.quote{position:absolute;width:360px;display:flex;gap:16px}
.quote-mark{flex:none;width:34px;height:34px;border-radius:50%;background:var(--gold);display:flex;align-items:center;justify-content:center}
.quote p{font-size:11px;line-height:1.55}
.quote .who{color:var(--gold);font-size:11px;margin-top:4px}

.partner-grid{position:absolute;top:3180px;left:210px;width:780px;display:grid;grid-template-columns:repeat(7,1fr);row-gap:34px;column-gap:20px;justify-items:center;align-items:center}
.badge{width:86px;height:34px;background:#cfcfcf;border-radius:4px}
.badge.round{width:40px;height:40px;border-radius:50%;background:#bdbdbd}
.badge.warm{background:#d9c9a3}

.site-footer{position:absolute;top:3440px;left:0;width:1200px;height:340px;background:var(--footer);color:#bdbdbd}
.site-footer h2{position:absolute;top:36px;left:0;width:1200px;text-align:center;color:var(--gold);font-size:21px;font-weight:400}
.footer-col{position:absolute;top:100px;font-size:11px;line-height:1.6}
.field{width:300px;height:28px;background:var(--white);border-radius:2px;margin-top:10px;color:#999;font-size:10px;padding:6px 10px}
.footer-col h5{color:var(--white);font-size:11px;letter-spacing:1px;margin-bottom:8px}
.socials{display:flex;gap:8px;margin-top:14px}
.socials span{width:22px;height:22px;border-radius:50%;background:var(--gold)}
.bottom-bar{position:absolute;top:3780px;left:0;width:1200px;height:40px;background:var(--footer-deep);color:#8a8a8a;font-size:10px;text-align:center;line-height:40px}
</style>
</head>
<body>

<header class="site-header">
  <div class="brand"><span class="brand-dot"></span>Quenmoor Leadership</div>
  <nav class="main-nav">
    <span class="active">HOME</span><span>ABOUT</span><span>SERVICES</span><span>TESTIMONIALS</span><span>CONTACT US</span>
  </nav>
</header>

<section class="hero">
  <div class="hero-shade" role="img" aria-label="Photo of a team meeting around a table in a bright office"></div>
  <p class="hero-intro">We help leaders build teams that perform, adapt and grow. Our consultants partner with owners and executives to turn people strategy into lasting business results.</p>
  <h1 class="hero-quote serif">“If opportunity doesn’t knock,<br>build a door”</h1>
  <div class="hero-cta"><span class="btn">Get Consultation</span></div>
</section>

<section class="mission">
  <h2 class="serif">GREAT COMPANIES SUCCEED<span>BY INVESTING IN THE RIGHT PEOPLE</span></h2>
  <p>For more than two decades we have guided growing companies through change by aligning leadership, culture and talent. We listen first, study how your organisation really works, and then build practical plans that your managers can own and carry forward every single day.</p>
  <p>At Quenmoor Leadership we believe people are your strongest advantage, and we measure our success by the lasting growth of your teams.</p>
</section>

<div class="photo" style="top:1000px;left:220px;width:380px;height:256px;background:linear-gradient(135deg,#4a4e52,#2f3336 60%,#6b6760)" role="img" aria-label="Photo of a presenter sketching a plan on a chalkboard"></div>
<div class="service abs" style="top:1006px;left:650px;width:340px">
  <h3>Talent Strategy</h3>
  <p>Recruiting the right people is only the beginning. We help you define the roles that matter most, attract strong candidates and build career paths that keep your best performers engaged, motivated and committed to the long term success of your business.</p>
  <span class="btn">Read More</span>
</div>

<div class="service right-align abs" style="top:1376px;left:210px;width:350px">
  <h3>Management Workshops</h3>
  <p>Our interactive workshops give managers the tools to lead with clarity and confidence. Each session blends proven frameworks with real examples from your own workplace, so new skills are practised, discussed and applied right away across every team.</p>
  <span class="btn">Read More</span>
</div>
<div class="photo" style="top:1370px;left:600px;width:380px;height:256px;background:linear-gradient(135deg,#b39a82,#8a6f58 55%,#d6c6b2)" role="img" aria-label="Photo of colleagues working together at a table"></div>

<div class="photo" style="top:1740px;left:220px;width:380px;height:256px;background:linear-gradient(135deg,#e8e4df,#cdbfb2 60%,#f3f0ec)" role="img" aria-label="Portrait photo of a smiling professional woman"></div>
<div class="service abs" style="top:1746px;left:650px;width:340px">
  <h3>Executive Coaching</h3>
  <p>One to one coaching helps senior leaders sharpen decisions, strengthen influence and navigate pressure. Together we set clear goals, work through real challenges and build habits that lift both personal performance and the results of the whole organisation.</p>
  <span class="btn">Read More</span>
</div>

<h2 class="section-title" style="top:2110px">Recent Quenmoor Blog Articles</h2>

<article class="blog-card" style="left:200px">
  <div class="thumb" style="background:linear-gradient(135deg,#d9d4cc,#9c958a)" role="img" aria-label="Photo of a team discussion in a modern office"></div>
  <h4>We Were Up For Your Role</h4>
  <div class="meta">June 12, 2017 · Leadership</div>
  <p>What happens when two strong candidates want the same promotion, and how leaders can keep both motivated.</p>
  <span class="more">Read More</span>
</article>
<article class="blog-card" style="left:470px">
  <div class="thumb" style="background:linear-gradient(135deg,#7a5a3c,#3e2f22)" role="img" aria-label="Photo of an interview in progress sign on a desk"></div>
  <h4>How to Get Great Interview Answers</h4>
  <div class="meta">May 28, 2017 · Hiring</div>
  <p>Better questions lead to better hires. Here are simple ways to learn more from every candidate you meet.</p>
  <span class="more">Read More</span>
</article>
<article class="blog-card" style="left:740px">
  <div class="thumb" style="background:linear-gradient(135deg,#e3ddd4,#a99b88)" role="img" aria-label="Photo of a man working on a laptop"></div>
  <h4>Dealing with Frustration at Work</h4>
  <div class="meta">May 10, 2017 · Coaching</div>
  <p>Frustration is normal, but how we respond shapes our teams. Practical steps to stay calm and focused.</p>
  <span class="more">Read More</span>
</article>
<div class="abs" style="top:2530px;left:0;width:1200px;text-align:center"><span class="btn">View All</span></div>

<section class="testimonials">
  <h2 class="section-title" style="top:40px">Testimonials</h2>
</section>
<div class="quote" style="top:2740px;left:220px">
  <span class="quote-mark"><svg width="14" height="12" viewBox="0 0 14 12"><path d="M0 12V7C0 3 2 1 5 0v2C3 3 3 5 3 6h3v6zM8 12V7c0-4 2-6 5-7v2c-2 1-2 3-2 4h3v6z" fill="#fff"/></svg></span>
  <div><p>Working with Quenmoor gave our leadership team a shared language and a clear plan. Turnover dropped within six months.</p><div class="who">— Daniel R. ★★★★★</div></div>
</div>
<div class="quote" style="top:2740px;left:640px">
  <span class="quote-mark"><svg width="14" height="12" viewBox="0 0 14 12"><path d="M0 12V7C0 3 2 1 5 0v2C3 3 3 5 3 6h3v6zM8 12V7c0-4 2-6 5-7v2c-2 1-2 3-2 4h3v6z" fill="#fff"/></svg></span>
  <div><p>The workshops were practical and energising. Our managers still use the tools every week with their teams.</p><div class="who">— Priya K. ★★★★★</div></div>
</div>
<div class="quote" style="top:2830px;left:220px">
  <span class="quote-mark"><svg width="14" height="12" viewBox="0 0 14 12"><path d="M0 12V7C0 3 2 1 5 0v2C3 3 3 5 3 6h3v6zM8 12V7c0-4 2-6 5-7v2c-2 1-2 3-2 4h3v6z" fill="#fff"/></svg></span>
  <div><p>Honest, insightful coaching that helped me step into a bigger role with real confidence and focus.</p><div class="who">— Laura M. ★★★★★</div></div>
</div>
<div class="quote" style="top:2830px;left:640px">
  <span class="quote-mark"><svg width="14" height="12" viewBox="0 0 14 12"><path d="M0 12V7C0 3 2 1 5 0v2C3 3 3 5 3 6h3v6zM8 12V7c0-4 2-6 5-7v2c-2 1-2 3-2 4h3v6z" fill="#fff"/></svg></span>
  <div><p>They took time to understand our culture before suggesting change. The results speak for themselves.</p><div class="who">— Tom H. ★★★★★</div></div>
</div>
<div class="abs" style="top:2950px;left:0;width:1200px;text-align:center"><span class="btn">View All</span></div>

<h2 class="section-title" style="top:3090px">Clients &amp; Partners</h2>
<div class="partner-grid">
  <span class="badge"></span><span class="badge"></span><span class="badge round"></span><span class="badge"></span><span class="badge warm"></span><span class="badge"></span><span class="badge round"></span>
  <span class="badge round"></span><span class="badge"></span><span class="badge"></span><span class="badge warm"></span><span class="badge"></span><span class="badge round"></span><span class="badge round"></span>
  <span class="badge"></span><span class="badge"></span><span class="badge round"></span><span class="badge"></span><span class="badge"></span><span class="badge"></span><span class="badge warm"></span>
</div>

<footer class="site-footer">
  <h2 class="serif">Learn to Inspire Employees and Unlock Their Maximum Potential</h2>
  <div class="footer-col" style="left:200px;width:320px">
    <p>Join our newsletter for monthly insights on leadership, hiring and team growth, sent straight to your inbox with no clutter.</p>
    <div class="field">Your Name</div>
    <div class="field">Email</div>
    <div style="margin-top:14px"><span class="btn">Subscribe Now</span></div>
  </div>
  <div class="footer-col" style="left:640px;width:360px">
    <h5>DOWNLOAD FREE INFORMATION</h5>
    <p>Get our practical guide to building engaged teams, with checklists and questions you can use with your managers this week.</p>
    <div class="brand" style="margin-top:22px"><span class="brand-dot"></span>Quenmoor Leadership</div>
    <div class="socials"><span></span><span></span><span></span><span></span></div>
  </div>
</footer>
<div class="bottom-bar">© Copyright 2017 Quenmoor Leadership · All Rights Reserved · www.corvelstrategy.example</div>

</body>
</html>
```